Human Resource Consultant's Website needs an Updated Look

I'm an HR Consultant based in Denver that caters to small business owners. I like my logo, and the existing content (though open to editorial suggestions) but would like to reformat my site and possibly update graphics. I want to be able to manage content moving forward. PLWTAdvisory.com

Target Market(s)

Small business owners with 10-500 employees in Metro Denver

Coding

Coded - Design and coding required

Font styles to use
Other font styles liked:
• Closer to existing font but open to suggestions

Colors

Designer to choose colors to be used in the design.

Requirements
Must have
• Links on landing page to other pages
• Visual appeal to younger demographic found in the small to medium sized business owner
• Scroll down rather than use the clunky "ladder" tabs I see now
• Color palate that compliments logo
Nice to have
• Pages that scroll down, links to page content on the first page,
Should not have
• Hate the standard employee-employer photos on most HR websites. Would prefer to use illustrations over the typical photos

```html
<!DOCTYPE html>
<html lang="en">
<head>
<meta charset="utf-8">
<title>Whitfield HR Advisory</title>
<link rel="stylesheet" href="https://fonts.googleapis.com/css2?family=Tinos:wght@400;700&family=Open+Sans:wght@400;600;700&display=swap">
<style>
:root{
  --green:#8dc63f;
  --green-dark:#4b5a1d;
  --blue:#1f5f9e;
  --blue-deep:#1b5a95;
  --blue-field:#164a7d;
  --blue-footer:#12365c;
  --grey-bg:#e4e4e4;
  --text:#6f6f6f;
  --ink:#333;
  --white:#fff;
}
*{margin:0;padding:0;box-sizing:border-box}
html,body{width:1200px;height:3939px;overflow:hidden}
body{position:relative;background:var(--white);font-family:"Open Sans",Arial,sans-serif;color:var(--text)}
.abs{position:absolute}

/* header */
.site-header{left:0;top:0;width:1200px;height:105px}
.brand{left:180px;top:24px;display:flex;align-items:center;gap:14px}
.brand-dot{width:56px;height:56px;border-radius:50%;background:var(--green)}
.brand-name{font-family:"Tinos",serif;font-size:28px;color:var(--blue);line-height:1}
.nav{right:180px;top:42px;display:flex;gap:22px;font-size:14px;font-weight:600;color:var(--blue)}
.nav .active{color:var(--green)}

/* hero */
.hero-art{left:545px;top:130px;width:555px;height:480px;border-radius:8px;background:radial-gradient(circle at 50% 50%,#fff 0,#f1f3f5 45%,#e4e8ec 100%)}
.hero-title{left:180px;top:236px;width:350px;z-index:2;font-family:"Tinos",serif;font-weight:400;font-size:37px;line-height:44px;color:var(--blue);white-space:nowrap}
.hero-title span{color:var(--green)}
.hero-text{left:180px;top:330px;width:355px;font-size:17px;line-height:24px;color:#8a8a8a}
.slider-dots{left:186px;top:428px;display:flex;gap:6px;align-items:center}
.slider-dots i{display:block;width:9px;height:9px;border-radius:50%;background:#ccc}
.slider-dots .arrow{width:17px;height:17px;background:#999}
.slider-dots .on{background:#888}

/* approach */
.approach-bg{left:0;top:620px}
.section-mark{width:40px;height:40px;border-radius:50%;border:3px solid currentColor}
.approach .section-mark{left:580px;top:665px;color:var(--white)}
.approach-title{left:0;width:1200px;top:714px;text-align:center;font-family:"Tinos",serif;font-weight:400;font-size:34px;color:var(--white)}
.approach-intro{left:200px;width:800px;top:764px;text-align:center;font-size:17px;line-height:26px;color:var(--white)}
.approach-item{width:380px;display:flex;gap:20px}
.tick{flex:none;width:48px;height:48px}
.approach-item h3{font-family:"Tinos",serif;font-weight:400;font-size:16px;color:var(--white);letter-spacing:.5px;margin-top:4px}
.approach-item p{font-size:14px;line-height:20px;color:#f4fbe8;margin-top:6px}
.btn{display:block;text-align:center;font-family:"Tinos",serif;font-size:15px;letter-spacing:.5px;color:var(--white);border-radius:22px}
.btn-dark{background:var(--green-dark);left:525px;top:1247px;width:147px;height:36px;line-height:36px}
.btn-green{background:var(--green);width:152px;height:35px;line-height:35px}

/* services */
.services .section-mark{left:586px;top:1372px;width:30px;height:30px;color:#bbb}
.section-title{left:0;width:1200px;text-align:center;font-family:"Tinos",serif;font-weight:400;font-size:32px;color:var(--blue)}
.service-title{font-family:"Tinos",serif;font-weight:400;font-size:27px;line-height:31px;color:var(--ink)}
.service-sub{font-size:14px;color:var(--blue)}
.chev{list-style:none}
.chev li{position:relative;padding-left:14px;font-size:13px;color:#555;line-height:24px}
.chev li::before{content:"";position:absolute;left:0;top:9px;width:6px;height:6px;border-top:2px solid var(--green);border-right:2px solid var(--green);transform:rotate(45deg)}
.pm-list li{color:var(--blue);font-size:14px;line-height:22px}
.pm-list li p{color:#444;font-size:11px;line-height:15px;margin:3px 0 10px -14px}
.art-block{border-radius:12px;background:linear-gradient(160deg,#eef6e2,#e3eef8)}

/* blogs */
.blogs-bg{left:0;top:2672px;width:1200px;height:620px;background:var(--grey-bg)}
.blogs .section-mark{left:586px;top:2712px;width:30px;height:30px;color:#aaa}
.card{width:263px;height:299px;background:var(--white);border:1px solid #ccc;top:2831px}
.card-art{height:171px;position:relative}
.card-date{position:absolute;left:81px;bottom:0;width:100px;height:22px;line-height:22px;text-align:center;background:var(--green);color:var(--white);font-size:11px}
.card h4{text-align:center;font-weight:400;font-size:16px;color:var(--ink);margin-top:14px}
.card p{text-align:center;font-size:9.5px;line-height:13px;color:#777;margin:8px 26px 0}
.card .more{display:block;text-align:center;font-size:9px;font-weight:700;color:var(--blue);margin-top:12px}

/* contact */
.contact-bg{left:0;top:3240px}
.contact .section-mark{left:583px;top:3262px;width:34px;height:34px;color:var(--white)}
.contact-title{top:3302px;color:var(--white);font-size:32px}
.contact-line{left:0;width:1200px;text-align:center;color:var(--white)}
.field{background:var(--blue-field);border:1px solid #2b6aa6;color:#d8e4f0;font-size:13px;padding:10px 16px}
.btn-submit{left:525px;top:3755px;width:153px;height:38px;line-height:38px;background:var(--green);border-radius:2px;font-size:16px}

/* footer */
.site-footer{left:0;top:3860px;width:1200px;height:79px;background:var(--blue-footer)}
.copyright{left:184px;top:30px;font-size:13px;color:#c9d6e4}
.social{right:170px;top:28px;display:flex;gap:20px}
.social i{display:block;width:18px;height:18px;border-radius:50%;background:#c9d6e4}
</style>
</head>
<body>

<header class="site-header abs">
  <div class="brand abs"><span class="brand-dot"></span><span class="brand-name">Whitfield HR Advisory</span></div>
  <nav class="nav abs"><span class="active">HOME</span><span>MY APPROACH</span><span>MY SERVICES</span><span>PAULA</span><span>CONTACT ME</span></nav>
</header>

<section class="hero">
  <div class="hero-art abs" role="img" aria-label="Illustration of a team meeting around a conference table seen from above, with charts and laptops"></div>
  <h1 class="hero-title abs">HR AND BUSINESS<br><span>CONSULTANT</span></h1>
  <p class="hero-text abs">Human capital is the wealth an organization possesses, derived from its people, which is critical to its economic success.</p>
  <div class="slider-dots abs"><i class="arrow"></i><i class="on"></i><i></i><i></i><i></i><i class="arrow"></i></div>
</section>

<section class="approach">
  <svg class="approach-bg abs" width="1200" height="720" viewBox="0 0 1200 720" aria-hidden="true">
    <path d="M0 90 Q600 -40 1200 90 L1200 540 Q600 800 0 540 Z" fill="#8dc63f"/>
    <path d="M40 610 Q600 760 1160 610" fill="none" stroke="#1f5f9e" stroke-width="7"/>
  </svg>
  <div class="section-mark abs"></div>
  <h2 class="approach-title abs">MY APPROACH</h2>
  <p class="approach-intro abs">Entrepreneurs are innovative risk-taking business leaders. You had an idea and ran with it! But when you looked back, were your employees following?&nbsp; If not, partner with me to…</p>

  <div class="approach-item abs" style="left:197px;top:868px">
    <svg class="tick" viewBox="0 0 48 48"><circle cx="24" cy="24" r="22" fill="none" stroke="#fff" stroke-width="2"/><path d="M14 25l7 7 13-15" fill="none" stroke="#fff" stroke-width="2.5"/></svg>
    <div><h3>HUMAN RESOURCES EXPERTISE</h3><p>building knowledge of HR laws, regulations, and best practices</p></div>
  </div>
  <div class="approach-item abs" style="left:630px;top:868px">
    <svg class="tick" viewBox="0 0 48 48"><circle cx="24" cy="24" r="22" fill="none" stroke="#fff" stroke-width="2"/><path d="M14 25l7 7 13-15" fill="none" stroke="#fff" stroke-width="2.5"/></svg>
    <div><h3>STRATEGY</h3><p>setting goals and leading individuals and teams towards aligned, successful results</p></div>
  </div>
  <div class="approach-item abs" style="left:197px;top:994px">
    <svg class="tick" viewBox="0 0 48 48"><circle cx="24" cy="24" r="22" fill="none" stroke="#fff" stroke-width="2"/><path d="M14 25l7 7 13-15" fill="none" stroke="#fff" stroke-width="2.5"/></svg>
    <div><h3>LEADERSHIP</h3><p>discussing different styles to complement one's own</p></div>
  </div>
  <div class="approach-item abs" style="left:630px;top:994px">
    <svg class="tick" viewBox="0 0 48 48"><circle cx="24" cy="24" r="22" fill="none" stroke="#fff" stroke-width="2"/><path d="M14 25l7 7 13-15" fill="none" stroke="#fff" stroke-width="2.5"/></svg>
    <div><h3>COMMUNICATION</h3><p>crystallizing messages to individuals and groups</p></div>
  </div>
  <div class="approach-item abs" style="left:197px;top:1124px">
    <svg class="tick" viewBox="0 0 48 48"><circle cx="24" cy="24" r="22" fill="none" stroke="#fff" stroke-width="2"/><path d="M14 25l7 7 13-15" fill="none" stroke="#fff" stroke-width="2.5"/></svg>
    <div><h3>RELATIONSHIP MANAGEMENT</h3><p>helping to develop collaborative networks</p></div>
  </div>
  <div class="approach-item abs" style="left:630px;top:1124px">
    <svg class="tick" viewBox="0 0 48 48"><circle cx="24" cy="24" r="22" fill="none" stroke="#fff" stroke-width="2"/><path d="M14 25l7 7 13-15" fill="none" stroke="#fff" stroke-width="2.5"/></svg>
    <div><h3>BUSINESS ACUMEN</h3><p>highlighting ways to improve return on investments, particularly with respect to human capital</p></div>
  </div>
  <a class="btn btn-dark abs">LEARN MORE</a>
</section>

<section class="services">
  <div class="section-mark abs"></div>
  <h2 class="section-title abs" style="top:1422px">MY SERVICES</h2>

  <h3 class="service-title abs" style="left:184px;top:1515px">HR PROJECT MANAGER</h3>
  <ul class="chev pm-list abs" style="left:184px;top:1560px;width:510px">
    <li>Financial Analysis of HR Metrics<p>Analyzing business plans and P&amp;Ls, identifying and establishing HR metrics meaningful to business owners, partnering to evaluate the return on investment (ROI) with respect to human capital</p></li>
    <li>Talent SWOT Analysis<p>Determining where talent is Strong or Weak and where the Opportunities or Threats lie</p></li>
    <li>Improving Organizational Efficiencies and Effectiveness<p>Providing analysis of jobs and processes to improve job satisfaction, organizational culture, ROI and compliance</p></li>
    <li>Strategic Compensation and Rewards Programs<p>Ensuring competitiveness based on current resources and planning for growth</p></li>
  </ul>
  <a class="btn btn-green abs" style="left:189px;top:1830px">LEARN MORE</a>
  <div class="art-block abs" style="left:743px;top:1523px;width:255px;height:263px" role="img" aria-label="Line icon of a manager connected to a team of three people"></div>

  <div class="art-block abs" style="left:223px;top:1956px;width:237px;height:250px" role="img" aria-label="Line icon of a trainer presenting a rising chart to two attendees"></div>
  <h3 class="service-title abs" style="left:583px;top:1938px">TRAINER AND FACILITATOR</h3>
  <p class="service-sub abs" style="left:583px;top:1982px">Topics relevant to your organization – as you need it.</p>
  <ul class="chev abs" style="left:583px;top:2012px">
    <li>HR's Impact on the Bottom Line</li><li>Human Capital Strategies</li><li>Employment Law</li><li>Leadership Competencies</li><li>Vision/Mission/Value Statements</li><li>Communication</li><li>Workplace Etiquette</li>
  </ul>
  <ul class="chev abs" style="left:827px;top:2012px">
    <li>Performance Management</li><li>Organizational Design and Development</li><li>Strategic Compensation and Rewards</li><li>Employee Engagement</li><li>Organizational Culture</li><li>Managing Multiple Generations</li><li>Avoiding Unionization</li>
  </ul>
  <a class="btn btn-green abs" style="left:572px;top:2208px">LEARN MORE</a>

  <h3 class="service-title abs" style="left:189px;top:2328px">HR AND BUSINESS<br>CONSULTANT</h3>
  <p class="service-sub abs" style="left:189px;top:2402px">Good advice – as you need it.</p>
  <ul class="chev abs" style="left:189px;top:2434px">
    <li>Strategic Planning</li><li>Employment Law</li><li>Conflict Resolution</li><li>Investigations</li>
  </ul>
  <ul class="chev abs" style="left:420px;top:2434px">
    <li>Terminations</li><li>Talent Acquisition</li><li>Change Management</li><li>Sounding Board</li>
  </ul>
  <a class="btn btn-green abs" style="left:184px;top:2557px">LEARN MORE</a>
  <div class="art-block abs" style="left:743px;top:2303px;width:215px;height:270px" role="img" aria-label="Line icon of a lightbulb containing a gear"></div>
</section>

<section class="blogs">
  <div class="blogs-bg abs"></div>
  <div class="section-mark abs"></div>
  <h2 class="section-title abs" style="top:2760px">PLWT BLOGS</h2>

  <article class="card abs" style="left:189px">
    <div class="card-art" role="img" aria-label="Illustration of connected business gears and icons" style="background:linear-gradient(160deg,#eef1f4,#cfd8e2)"><span class="card-date">02 Aug 2017</span></div>
    <h4>Benefits and Beyond....</h4>
    <p>Notes on building a benefits plan that keeps small teams engaged and loyal.</p>
    <span class="more">READ MORE</span>
  </article>
  <article class="card abs" style="left:475px">
    <div class="card-art" role="img" aria-label="Illustration of a desk with laptop, charts and payment documents" style="background:linear-gradient(160deg,#6fb6d8,#2f7fb5)"><span class="card-date">02 Aug 2017</span></div>
    <h4>Beyond Comp and Benefits</h4>
    <p>Why pay alone rarely retains talent and what growing firms can offer instead.</p>
    <span class="more">READ MORE</span>
  </article>
  <article class="card abs" style="left:762px">
    <div class="card-art" role="img" aria-label="Illustration of office papers, magnifier and teamwork icons" style="background:linear-gradient(160deg,#f3f4f6,#c9d2da)"><span class="card-date">02 Aug 2017</span></div>
    <h4>Organizational Culture</h4>
    <p>Shaping shared values so every new hire knows how the company works.</p>
    <span class="more">READ MORE</span>
  </article>
</section>

<section class="contact">
  <svg class="contact-bg abs" width="1200" height="620" viewBox="0 0 1200 620" role="img" aria-label="Faint background illustration of people working toward goals">
    <defs><linearGradient id="contactFill" x1="0" y1="0" x2="0" y2="1"><stop offset="0" stop-color="#1f64a3"/><stop offset="1" stop-color="#174f86"/></linearGradient></defs>
    <path d="M0 95 Q600 -30 1200 95 L1200 620 L0 620 Z" fill="url(#contactFill)"/>
  </svg>
  <div class="section-mark abs"></div>
  <h2 class="section-title contact-title abs">CONTACT</h2>
  <p class="contact-line abs" style="top:3370px;font-size:16px">PAULA WHITFIELD – HR ADVISORY, LLC</p>
  <p class="contact-line abs" style="top:3400px;font-size:19px">
    <svg width="20" height="14" viewBox="0 0 20 14" style="vertical-align:-1px;margin-right:6px"><rect x="0.5" y="0.5" width="19" height="13" fill="#fff"/><path d="M1 1l9 7 9-7" fill="none" stroke="#1b5a95" stroke-width="1.5"/></svg>PWhitfield@PLWTAdvisory.com</p>
  <p class="contact-line abs" style="top:3436px;font-size:19px">
    <svg width="16" height="16" viewBox="0 0 24 24" style="vertical-align:-2px;margin-right:4px"><path d="M6.6 10.8a15 15 0 006.6 6.6l2.2-2.2c.3-.3.7-.4 1-.2 1.1.4 2.3.6 3.6.6.6 0 1 .4 1 1V20c0 .6-.4 1-1 1A17 17 0 013 4c0-.6.4-1 1-1h3.5c.6 0 1 .4 1 1 0 1.3.2 2.5.6 3.6.1.3 0 .7-.2 1z" fill="#fff"/></svg>720.555.0148</p>
  <p class="contact-line abs" style="top:3476px;font-size:16px">Contact me for a FREE Introductory Consultation!</p>

  <form class="abs" style="left:276px;top:3530px;width:656px">
    <div class="field abs" style="left:0;top:0;width:324px;height:42px">First Name</div>
    <div class="field abs" style="left:332px;top:0;width:324px;height:42px">Last Name</div>
    <div class="field abs" style="left:0;top:50px;width:324px;height:44px">Phone</div>
    <div class="field abs" style="left:332px;top:50px;width:324px;height:44px">Email</div>
    <div class="field abs" style="left:0;top:107px;width:656px;height:93px">Message</div>
  </form>
  <a class="btn btn-submit abs">SUBMIT</a>
</section>

<footer class="site-footer abs">
  <p class="copyright abs">© 2018 Company Name&nbsp; All right reserved</p>
  <div class="social abs" aria-label="Social media links"><i></i><i></i><i></i><i></i></div>
</footer>

</body>
</html>
```